National Virtual accounting firm needs website designed

I need a wordpress website design for a national virtual accounting firm. I will upload my business card, logo, and postcards that I have had designed and followed the same style. I want a similar style to be followed so I can keep the running theme similar.

Services include:

Tax Services:
Tax preparation and planning services for Individuals, businesses, estates, and nonprofits
Full Service Payroll for Businesses
ODV Audit Representation

Consulting:
Entity Selection & Restructuring
Financial Projections & Forecasts
Retirement Planning
IPO Readiness

Accounting:
Bookkeeping
Reviews and Compilations
Payroll Services

Other Services:
CFO Services
Compliance Services
Controller Services
Software Implementations for Brimlane, Corvanta, and Plivorn.

Target Market(s)

small to medium size businesses, and individuals

Industry/Entity Type

accounting firms

Font styles to use
Sans Serif

Colors
59FF00
82FF00
B8FF75
E3FFCB
F4FFEA

Requirements
Must have
• Color schematics from the logo and post cards/business cards

```html
<!DOCTYPE html>
<html lang="en">
<head>
<meta charset="utf-8">
<title>Vantrex — Business Advisors and Consultants</title>
<link href="https://fonts.googleapis.com/css2?family=Alfa+Slab+One&family=Montserrat:wght@500;600;700&family=Oswald:wght@500&family=Roboto:ital,wght@0,400;0,500;0,700;1,400&display=swap" rel="stylesheet">
<style>
:root{
  --green:#4bb848;
  --green-bright:#62c93a;
  --green-dark:#17853a;
  --yellow:#ffc814;
  --yellow-soft:#fcd628;
  --mint:#f1fdea;
  --ink:#111111;
  --text:#333333;
  --muted:#666666;
  --white:#ffffff;
  --card:#f4f4f4;
  --black:#000000;
}
*{margin:0;padding:0;box-sizing:border-box}
html,body{width:1200px;height:4132px;overflow:hidden}
body{position:relative;background:var(--white);font-family:"Roboto",Arial,sans-serif;color:var(--text)}
.abs{position:absolute}
.display{font-family:"Alfa Slab One",Georgia,serif;font-weight:400;color:var(--ink);letter-spacing:.5px}
.btn{position:absolute;display:flex;align-items:center;justify-content:center;border-radius:14px;font-family:"Alfa Slab One",Georgia,serif;font-size:10px;letter-spacing:.3px;color:var(--white);background:var(--green);text-transform:uppercase;box-shadow:3px 3px 0 var(--yellow);white-space:nowrap}
.btn.yellow{background:var(--yellow);box-shadow:3px 3px 0 var(--green)}
.section-title{position:absolute;left:0;width:1200px;text-align:center;font-size:37px}

/* header */
.site-header{position:absolute;left:0;top:0;width:1200px;height:96px;background:var(--white);z-index:2}
.brand{position:absolute;display:flex;align-items:center;gap:10px;z-index:2}
.brand-dot{width:22px;height:22px;border-radius:50%;background:var(--yellow)}
.brand-name{font-family:"Alfa Slab One",Georgia,serif;font-size:29px;color:var(--ink)}
.topbar{position:absolute;left:398px;top:0;width:802px;height:35px;background:var(--green-bright);color:var(--white);font-size:12px}
.topbar .item{position:absolute;top:0;height:35px;display:flex;align-items:center;gap:10px}
.topbar .ico{width:24px;height:24px;border-radius:50%;background:var(--yellow);display:flex;align-items:center;justify-content:center}
.social{position:absolute;top:7px;width:21px;height:21px;border-radius:50%;background:var(--white)}
.nav{position:absolute;top:52px;font-size:10.5px;font-weight:500;color:var(--ink);text-transform:uppercase}

/* hero */
.hero-photo{position:absolute;left:0;top:96px;width:1200px;height:578px;background:linear-gradient(100deg,#6c7f98 0%,#a9b6c6 35%,#dfe5ec 60%,#9fb0c4 100%)}
.hero-eyebrow{position:absolute;left:162px;top:199px;font-family:"Alfa Slab One",Georgia,serif;font-size:16px;line-height:20px;color:var(--yellow);z-index:2}
.hero-title{position:absolute;left:160px;top:220px;width:420px;font-family:"Alfa Slab One",Georgia,serif;font-weight:400;font-size:39px;line-height:44px;color:var(--white);white-space:nowrap;z-index:2}
.badge{position:absolute;left:531px;top:595px;width:134px;height:134px;border-radius:50%;background:var(--yellow);border:4px solid var(--white);display:flex;align-items:center;justify-content:center;text-align:center;font-family:"Oswald",Arial,sans-serif;font-size:18px;line-height:27px;color:#4b3a00;text-transform:uppercase;z-index:5}

/* why choose */
.why{position:absolute;left:0;top:674px;width:1200px;height:609px;background:var(--mint)}
.feature{position:absolute;top:246px;width:240px;height:240px;border-radius:50%;background:var(--white);box-shadow:0 6px 14px rgba(0,0,0,.12);display:flex;flex-direction:column;align-items:center;justify-content:center;gap:16px;font-family:"Alfa Slab One",Georgia,serif;font-size:16px;color:var(--green)}
.feature.active{background:var(--green);color:var(--white);box-shadow:none}

/* services */
.service{position:absolute;top:1455px;width:210px;text-align:center}
.service.raised{background:var(--white);height:285px;box-shadow:0 4px 12px rgba(0,0,0,.15)}
.service-photo{width:210px;height:138px}
.service h3{margin-top:13px;font-family:"Alfa Slab One",Georgia,serif;font-weight:400;font-size:14px;color:var(--ink)}
.service p{margin:8px auto 0;width:190px;font-size:10.5px;line-height:18px;color:var(--text)}
.service .btn{position:relative;margin:14px auto 0;width:103px;height:26px}

/* about */
.about-photo{position:absolute;left:560px;top:1805px;width:640px;height:478px;background:linear-gradient(90deg,#7a6a1c 0%,#243a66 40%,#dfe7f2 55%,#1e2f55 75%,#6a5a18 100%)}
.about-text{position:absolute;left:99px;top:1986px;width:436px;font-size:10.5px;line-height:20.6px;color:var(--white)}

/* testimonials */
.quote{position:absolute;left:238px;top:2470px;width:728px;text-align:center;font-style:italic;font-size:17px;line-height:30.5px;color:#2b2b2b}
.quote-mark{font-family:"Alfa Slab One",Georgia,serif;font-style:normal;font-size:60px;line-height:0;color:var(--yellow);vertical-align:-22px}

/* blog */
.post{position:absolute;overflow:hidden;border-radius:6px}
.post.text{background:var(--card);padding:22px 13px 0}
.date{display:inline-block;padding:4px 14px;border-radius:10px;background:var(--green);color:var(--white);font-family:"Montserrat",Arial,sans-serif;font-weight:700;font-size:9px}
.post h4{font-family:"Montserrat",Arial,sans-serif;font-weight:600;font-size:12.5px;line-height:18px;color:var(--ink);margin-top:12px}
.post p{margin-top:8px;font-size:9.5px;line-height:18.5px;color:#555}
.post .overlay{position:absolute;left:0;bottom:0;width:100%;padding:0 13px 16px;background:linear-gradient(0deg,rgba(0,0,0,.75),rgba(0,0,0,0))}
.post .overlay h4{color:var(--white)}
.post.big .overlay{padding:0 22px 22px}
.post.big .overlay h4{font-size:21px;line-height:27px}

/* cta */
.cta{position:absolute;left:0;top:3385px;width:1200px;height:440px;background:linear-gradient(180deg,#ffd21e 0%,#ffcb12 100%)}
.cta p{position:absolute;left:270px;top:144px;width:660px;text-align:center;font-size:10.5px;line-height:22px;color:#fff6c0}

/* footer */
.footer-brand .brand-name{color:var(--white);font-size:38px}
.contact{position:absolute;top:3938px;display:flex;align-items:center;gap:16px;font-size:13px;line-height:19px;color:var(--white)}
.contact .ico{width:32px;height:32px;border-radius:50%;background:var(--green);display:flex;align-items:center;justify-content:center;flex:none}
.rule{position:absolute;left:162px;width:874px;height:1px;background:#555}
.foot-nav{position:absolute;top:4022px;left:0;width:1200px;display:flex;justify-content:center;gap:34px;font-size:10.5px;font-weight:500;color:var(--white);text-transform:uppercase}
.copyright{position:absolute;top:4084px;left:0;width:1200px;text-align:center;font-size:12px;color:var(--green)}
.copyright b{color:var(--yellow);font-weight:400}
</style>
</head>
<body>

<!-- Header -->
<header class="site-header">
  <div class="brand" style="left:166px;top:20px"><span class="brand-dot"></span><span class="brand-name">VANTREX</span></div>
  <div class="topbar">
    <div class="item" style="left:16px"><span class="ico"><svg width="12" height="12" viewBox="0 0 24 24"><path d="M6.6 10.8a15 15 0 0 0 6.6 6.6l2.2-2.2a1 1 0 0 1 1-.25 11.4 11.4 0 0 0 3.6.57 1 1 0 0 1 1 1V20a1 1 0 0 1-1 1A17 17 0 0 1 3 4a1 1 0 0 1 1-1h3.5a1 1 0 0 1 1 1c0 1.25.2 2.45.57 3.57a1 1 0 0 1-.25 1z" fill="#fff"/></svg></span>(555) 014-2270</div>
    <div class="item" style="left:172px"><span class="ico"><svg width="12" height="12" viewBox="0 0 24 24"><path d="M2 11l20-8-8 20-3-8z" fill="#fff"/></svg></span>hello@vantrex.com</div>
    <span class="social" style="left:514px"></span>
    <span class="social" style="left:545px"></span>
    <span class="social" style="left:576px"></span>
    <span class="social" style="left:607px"></span>
    <span class="social" style="left:638px"></span>
  </div>
  <span class="nav" style="left:403px">Home</span>
  <span class="nav" style="left:468px">About Us</span>
  <span class="nav" style="left:555px">Our Services</span>
  <span class="nav" style="left:664px">Why Choose Us</span>
  <span class="nav" style="left:784px">Contact Us</span>
  <span class="btn yellow" style="left:871px;top:45px;width:194px;height:27px">Shedule a free consult now</span>
</header>

<!-- Hero -->
<section>
  <div class="hero-photo" role="img" aria-label="Business collage: handshake and team photos set in hexagon frames over a blurred office scene"></div>
  <svg class="abs" style="left:0;top:430px" width="1200" height="260" viewBox="0 0 1200 260">
    <path d="M0 70 C 150 190, 420 230, 700 200 C 900 180, 1080 120, 1200 60 L1200 260 L0 260 Z" fill="#8ad65a"/>
    <path d="M0 96 C 160 205, 430 245, 700 222 C 900 205, 1080 150, 1200 100 L1200 260 L0 260 Z" fill="#4bb848"/>
    <path d="M0 150 C 180 235, 440 262, 700 246 C 900 232, 1080 190, 1200 150 L1200 260 L0 260 Z" fill="#f1fdea"/>
  </svg>
  <div class="hero-eyebrow">WELCOME TO VANTREX</div>
  <h1 class="hero-title">Why Settle for<br>Less When Your<br>Finances Could<br>be Exact?</h1>
  <span class="btn yellow" style="left:162px;top:411px;width:196px;height:26px">Shedule a free consult now</span>
</section>

<!-- Why choose us -->
<section class="why">
  <h2 class="display section-title" style="top:98px">WHY CHOOSE US</h2>
  <div class="feature" style="left:190px">
    <svg width="84" height="64" viewBox="0 0 84 64" fill="none" stroke="#4bb848" stroke-width="3">
      <path d="M26 8l3 6 6 1-4.5 4 1 6-5.5-3-5.5 3 1-6L17 15l6-1z"/><path d="M42 2l3 6 6 1-4.5 4 1 6-5.5-3-5.5 3 1-6L33 9l6-1z"/><path d="M58 8l3 6 6 1-4.5 4 1 6-5.5-3-5.5 3 1-6L49 15l6-1z"/>
      <circle cx="22" cy="38" r="6"/><circle cx="62" cy="38" r="6"/><circle cx="42" cy="36" r="7"/>
      <path d="M8 62c0-8 6-13 14-13s12 4 13 8M76 62c0-8-6-13-14-13s-12 4-13 8M27 62c0-9 7-15 15-15s15 6 15 15z"/>
    </svg>
    <span>EXPIRIENCED</span>
  </div>
  <div class="feature active" style="left:496px">
    <svg width="70" height="70" viewBox="0 0 70 70" fill="none" stroke="#fff" stroke-width="3">
      <rect x="32" y="4" width="30" height="18" rx="2"/><path d="M38 12h18"/>
      <circle cx="26" cy="24" r="7"/><path d="M14 50V40c0-5 5-8 12-8s12 3 12 8v4"/>
      <path d="M8 50h54M14 50v18M56 50v18M20 68h30"/>
    </svg>
    <span>PROFESSIONAL</span>
  </div>
  <div class="feature" style="left:793px">
    <svg width="76" height="70" viewBox="0 0 76 70" fill="none" stroke="#4bb848" stroke-width="3">
      <circle cx="42" cy="18" r="15"/><path d="M46 11h-6a3.5 3.5 0 0 0 0 7h4a3.5 3.5 0 0 1 0 7h-7M42 7v4M42 25v4"/>
      <rect x="4" y="44" width="12" height="22"/>
      <path d="M16 48h14c4 0 6 3 10 3h10a3 3 0 0 1 0 6H38M16 62h26l24-14a4 4 0 0 0-5-6l-12 7"/>
    </svg>
    <span>AFFORDABLE</span>
  </div>
</section>

<div class="badge">Business<br>Advisors and<br>Consultants</div>

<!-- Services -->
<section>
  <h2 class="display section-title" style="top:1372px">OUR SERVICES</h2>
  <article class="service" style="left:162px">
    <div class="service-photo" role="img" aria-label="Hands using a calculator over tax documents" style="background:linear-gradient(135deg,#c9b49a,#e9e6e0 55%,#3c3f47)"></div>
    <h3>TAX SERVICES</h3>
    <p>Lorem ipsum dolor sit amet, consectetur adipiscing elit, sed do eiusmod tempor incididunt ut labore et.</p>
    <span class="btn">Learn more</span>
  </article>
  <article class="service raised" style="left:383px">
    <div class="service-photo" role="img" aria-label="Two colleagues discussing papers at a desk" style="background:linear-gradient(135deg,#4a5a3c,#cfc6b2 50%,#2f3330)"></div>
    <h3>CONSULTING</h3>
    <p>Lorem ipsum dolor sit amet, consectetur adipiscing elit, sed do eiusmod tempor incididunt ut labore et.</p>
    <span class="btn yellow">Learn more</span>
  </article>
  <article class="service" style="left:605px">
    <div class="service-photo" role="img" aria-label="Team reviewing charts and reports on a white table" style="background:linear-gradient(135deg,#e8e8e8,#f6f6f6 50%,#8a5a3a)"></div>
    <h3>ACCOUNTING</h3>
    <p>Lorem ipsum dolor sit amet, consectetur adipiscing elit, sed do eiusmod tempor incididunt ut labore et.</p>
    <span class="btn">Learn more</span>
  </article>
  <article class="service" style="left:826px">
    <div class="service-photo" role="img" aria-label="Hand working on a calculator beside a laptop" style="background:linear-gradient(135deg,#d8dde3,#f2f2f2 45%,#6a6f78)"></div>
    <h3>OTHER SERVICES</h3>
    <p>Lorem ipsum dolor sit amet, consectetur adipiscing elit, sed do eiusmod tempor incididunt ut labore et.</p>
    <span class="btn">Learn more</span>
  </article>
</section>

<!-- About -->
<section>
  <div class="about-photo" role="img" aria-label="Smiling businesswoman in glasses and a navy blazer with arms crossed"></div>
  <svg class="abs" style="left:0;top:1805px" width="680" height="478" viewBox="0 0 680 478">
    <defs><linearGradient id="aboutGreen" x1="0" x2="1"><stop offset="0" stop-color="#4bb848"/><stop offset="1" stop-color="#17853a"/></linearGradient></defs>
    <path d="M0 0 H590 C 660 150, 660 330, 590 478 H0 Z" fill="#62c93a"/>
    <path d="M0 0 H560 C 628 150, 628 330, 560 478 H0 Z" fill="url(#aboutGreen)"/>
  </svg>
  <h2 class="display abs" style="left:128px;top:1896px;font-size:37px;color:#fff">ABOUT VANTREX</h2>
  <p class="about-text">Lorem ipsum dolor sit amet, consectetur adipiscing elit, sed do eiusmod tempor incididunt ut labore et dolore magna aliqua. Quis ipsum suspendisse ultrices gravida. Risus commodo viverra maecenas accumsan lacus vel facilisis. perspiciatis unde omnis iste natus error sit voluptatem accusantium doloremque laudantium, totam rem aperiam, eaque ipsa quae ab illo inventore veritatis et quasi architecto beatae vitae dicta sunt explicabo. Nemo enim ipsam voluptatem quia voluptas sit aspernatur aut odit aut fugit, sed quia consequuntur magni dolores eos qui ratione voluptatem sequi nesciunt. Neque porro quisquam est, qui dolorem ipsum quia dolor sit amet, consectetur, adipisci velit, sed quia non numquam eius modi tempora incidunt ut labore et dolore magnam aliquam quaerat voluptatem. perspiciatis unde omnis iste natus error sit voluptatem accusantium doloremque laudantium.</p>
  <span class="btn yellow" style="left:99px;top:2192px;width:103px;height:26px">Learn more</span>
</section>

<!-- Testimonials -->
<section class="abs" style="left:0;top:2283px;width:1200px;height:449px;background:var(--mint)">
  <h2 class="display section-title" style="top:64px">OUR CLIENT TESTIMONIALS</h2>
  <svg class="abs" style="left:152px;top:268px" width="22" height="36" viewBox="0 0 22 36"><path d="M18 2L4 18l14 16" fill="none" stroke="#333" stroke-width="2"/></svg>
  <svg class="abs" style="left:1026px;top:268px" width="22" height="36" viewBox="0 0 22 36"><path d="M4 2l14 16L4 34" fill="none" stroke="#333" stroke-width="2"/></svg>
</section>
<p class="quote"><span class="quote-mark">“</span> Lorem ipsum dolor sit amet, consectetur adipiscing elit, sed do eiusmod tempor incididunt ut labore et dolore magna aliqua. Ut enim ad minim veniam, quis nostrud exercitation ullamco laboris nisi ut aliquip ex ea commodo consequat. Duis aute irure dolor in reprehenderit in voluptate velit esse cillum dolore eu fugiat nulla pariatur. Excepteur sint occaecat cupidatat non proident, sunt in culpa qui officia deserunt mollit anim. <span class="quote-mark">”</span></p>
<div class="abs" style="left:0;top:2645px;width:1200px;text-align:center;font-family:'Alfa Slab One',Georgia,serif;font-size:11px;color:var(--green)">-Dana Whitfield</div>
<div class="abs" style="left:0;top:2664px;width:1200px;text-align:center;font-style:italic;font-size:10px;color:#555">Lorem ipsum dolor sit amet, consectetur</div>

<!-- Blog -->
<section>
  <h2 class="display section-title" style="top:2798px">OUR LATEST BLOG</h2>
  <article class="post big" style="left:164px;top:2892px;width:421px;height:412px;background:linear-gradient(135deg,#c9ccd0,#e3e4e5 40%,#3a3d44)" role="img" aria-label="Young man in a suit working at a laptop in an office">
    <div class="overlay"><span class="date">MAR 05,2023</span><h4>Lorem ipsum dolor sit amet consectetur adipiscing.</h4></div>
  </article>
  <article class="post text" style="left:600px;top:2892px;width:210px;height:257px">
    <span class="date">MAR 05,2023</span>
    <h4>Lorem ipsum dolor sit amet consectetur adipiscing.</h4>
    <p>Lorem ipsum dolor sit amet, consectetur adipiscing elit, sed do eiusmod tempor incididunt ut labore et dolore magna aliqua. Quis ipsum suspendisse ultrices gravida. Risus commodo viverra maec enas accumsan lacus vel facilisis.</p>
  </article>
  <article class="post" style="left:600px;top:3162px;width:210px;height:142px;background:linear-gradient(135deg,#d9d4cc,#8d7a6a 50%,#3b3a3e)" role="img" aria-label="Colleagues in a meeting around a table">
    <div class="overlay"><span class="date">MAR 05,2023</span><h4>Lorem ipsum dolor sit amet consectetur adipiscing.</h4></div>
  </article>
  <article class="post" style="left:826px;top:2892px;width:210px;height:143px;background:linear-gradient(135deg,#3b4a66,#6a7690 50%,#2a2c33)" role="img" aria-label="Business team reviewing documents together">
    <div class="overlay"><span class="date">MAR 05,2023</span><h4>Lorem ipsum dolor sit amet consectetur adipiscing.</h4></div>
  </article>
  <article class="post text" style="left:826px;top:3052px;width:210px;height:252px">
    <span class="date">MAR 05,2023</span>
    <h4>Lorem ipsum dolor sit amet consectetur adipiscing.</h4>
    <p>Lorem ipsum dolor sit amet, consectetur adipiscing elit, sed do eiusmod tempor incididunt ut labore et dolore magna aliqua. Quis ipsum suspendisse ultrices gravida. Risus commodo viverra maec enas accumsan lacus vel facilisis.</p>
  </article>
</section>

<!-- Call to action -->
<section class="cta">
  <h2 class="display section-title" style="top:54px;color:#fff">HAVE ANY QUESTIONS?</h2>
  <p>Lorem ipsum dolor sit amet, consectetur adipiscing elit, sed do eiusmod tempor incididunt ut labore et dolore magna aliqua. Quis ipsum suspendisse ultrices gravida. Risus commodo viverra maecenas accumsan lacus vel facilisis.</p>
  <span class="btn" style="left:524px;top:198px;width:194px;height:26px">Shedule a free consult now</span>
</section>

<!-- Footer -->
<footer>
  <svg class="abs" style="left:0;top:3680px" width="1200" height="452" viewBox="0 0 1200 452">
    <path d="M0 180 C 300 40, 700 0, 1200 40 V452 H0 Z" fill="#8ad65a"/>
    <path d="M0 210 C 300 80, 700 40, 1200 70 V452 H0 Z" fill="#4bb848"/>
    <path d="M0 260 C 300 120, 700 80, 1200 110 V452 H0 Z" fill="#000"/>
  </svg>
  <div class="brand footer-brand" style="left:488px;top:3838px"><span class="brand-dot" style="width:26px;height:26px"></span><span class="brand-name">VANTREX</span></div>
  <div class="contact" style="left:194px">
    <span class="ico"><svg width="16" height="16" viewBox="0 0 24 24"><path d="M12 2a7 7 0 0 0-7 7c0 5 7 13 7 13s7-8 7-13a7 7 0 0 0-7-7zm0 9.5A2.5 2.5 0 1 1 12 6.5a2.5 2.5 0 0 1 0 5z" fill="#fff"/></svg></span>
    <span>123 Lorem ipsum dolor sit amet<br>consectetur adipiscing elit.</span>
  </div>
  <div class="contact" style="left:530px;font-size:12px">
    <span class="ico"><svg width="15" height="15" viewBox="0 0 24 24"><path d="M6.6 10.8a15 15 0 0 0 6.6 6.6l2.2-2.2a1 1 0 0 1 1-.25 11.4 11.4 0 0 0 3.6.57 1 1 0 0 1 1 1V20a1 1 0 0 1-1 1A17 17 0 0 1 3 4a1 1 0 0 1 1-1h3.5a1 1 0 0 1 1 1c0 1.25.2 2.45.57 3.57a1 1 0 0 1-.25 1z" fill="#fff"/></svg></span>
    <span>Office: (555) 014-2270<br>Fax: (555) 014-3391</span>
  </div>
  <div class="contact" style="left:812px">
    <span class="ico"><svg width="15" height="15" viewBox="0 0 24 24"><path d="M2 11l20-8-8 20-3-8z" fill="#fff"/></svg></span>
    <span><span style="font-size:11px">Email Us</span><br>hello@vantrex.com</span>
  </div>
  <div class="rule" style="top:4002px"></div>
  <nav class="foot-nav"><span>Home</span><span>About Us</span><span>Our Services</span><span>Why Choose Us</span><span>Blog</span><span>Contact Us</span></nav>
  <div class="rule" style="top:4058px"></div>
  <div class="copyright">Copyright © 2023 <b>Vantrex</b>. All Rights Reserved. Imprint | Cookie Policy | Sitemap</div>
</footer>

</body>
</html>
```